mediation practice website build

Looking to create a website for new civil mediation practice. Pages would be "home", "about us", "about mediation", "scheduling" (perhaps with some kind of calendar function), "contact us". Would love to be able to update content/text myself.
Reason: Still working on revisions with the designs submitted. Thanks to all for your submissions!
Small to midsize businesses and attorneys representing those size businesses in pending disputes.
Build

```html
<!DOCTYPE html>
<html lang="en">
<head>
<meta charset="utf-8">
<title>Oakridge Mediation — Home</title>
<link rel="stylesheet" href="https://fonts.googleapis.com/css2?family=Arimo:wght@400;700&display=swap">
<style>
  :root {
    --page-bg: #e6e6e6;
    --card-bg: #ffffff;
    --navy: #2c3c66;
    --brand-blue: #1f4a82;
    --heading-blue: #1c4f91;
    --text: #1a1a1a;
    --nav-dark: #3b4562;
    --nav-dark-top: #66708c;
    --nav-active: #c9c25a;
    --nav-active-top: #ecea9a;
    --peach-light: #f4d2c0;
    --peach-mid: #e2a59c;
    --peach-deep: #b96a6c;
    --office-light: #e9e9ec;
    --office-mid: #9a9aa2;
    --office-dark: #3d3f4a;
    --arrow-grey: #9ea3ad;
    --social-navy: #3b5590;
    --social-sky: #55b7de;
  }
  * { box-sizing: border-box; margin: 0; padding: 0; }
  html, body {
    width: 1200px; height: 900px; overflow: hidden;
    background: var(--page-bg);
    font-family: "Arimo", Arial, sans-serif;
  }
  .site {
    position: absolute; left: 36px; top: 44px;
    width: 1124px; height: 816px;
    background: var(--card-bg);
    border-radius: 22px;
    overflow: hidden;
  }
  .masthead { position: absolute; left: 0; top: 0; width: 1124px; height: 214px; }
  .masthead-photo { position: absolute; inset: 0; }
  .brand {
    position: absolute; left: 30px; top: 30px;
    color: var(--brand-blue);
    font-weight: 700; font-size: 54px; line-height: 62px;
    letter-spacing: 3px; text-transform: uppercase;
  }
  .main-nav { position: absolute; top: 90px; left: 492px; display: flex; gap: 22px; }
  .main-nav a {
    display: block; height: 38px; line-height: 38px;
    padding: 0 22px;
    border-radius: 19px;
    color: #fff; text-decoration: none;
    font-size: 13px; letter-spacing: 0.8px; text-transform: uppercase;
    background: linear-gradient(var(--nav-dark-top), var(--nav-dark) 55%);
    box-shadow: 0 2px 3px rgba(0,0,0,0.35);
  }
  .main-nav a.is-current {
    background: linear-gradient(var(--nav-active-top), var(--nav-active) 60%);
    padding: 0 20px;
  }
  .slider {
    position: absolute; left: 84px; top: 248px;
    width: 972px; height: 282px;
    border: 4px solid var(--navy); border-radius: 10px;
    overflow: hidden; display: flex;
  }
  .slide { flex: 1; height: 100%; }
  .slide-meeting { background: linear-gradient(100deg, var(--office-light) 0%, #c8c4c0 45%, var(--office-mid) 100%); }
  .slide-handshake { background: linear-gradient(80deg, var(--office-dark) 0%, #6c7080 40%, #d4d8e0 100%); }
  .slider-arrow { position: absolute; top: 366px; }
  .slider-arrow.prev { left: 54px; }
  .slider-arrow.next { left: 1024px; }
  .feature { position: absolute; top: 572px; width: 540px; height: 170px; }
  .feature-1 { left: 24px; }
  .feature-2 { left: 578px; }
  .feature-thumb {
    position: absolute; left: 0; top: 0; width: 202px; height: 140px;
    border: 4px solid var(--navy); border-radius: 12px;
    background: linear-gradient(90deg, #4e5466 0%, #c7ccd6 50%, #5a6072 100%);
  }
  .feature-title {
    position: absolute; left: 224px; top: 2px; width: 300px;
    color: var(--heading-blue); font-size: 19px; font-weight: 700; line-height: 23px;
  }
  .feature-body {
    position: absolute; left: 224px; top: 68px; width: 316px;
    color: var(--text); font-size: 11.5px; line-height: 15px;
  }
  .feature-body .lead { margin-bottom: 1px; }
  .feature-more {
    position: absolute; right: 0; top: 148px;
    color: var(--heading-blue); font-size: 12px; font-weight: 700; text-decoration: none;
  }
  .social { position: absolute; top: 770px; right: 22px; display: flex; gap: 14px; align-items: center; }
  .social a { font-size: 19px; font-weight: 700; text-decoration: none; }
  .social .friendnet { color: var(--social-navy); }
  .social .chirpline { color: var(--social-sky); }
</style>
</head>
<body>
<div class="site">
  <header class="masthead">
    <svg class="masthead-photo" width="1124" height="214" viewBox="0 0 1124 214" role="img" aria-label="Soft-focus photograph of ripe peaches">
      <defs>
        <linearGradient id="peachTone" x1="0" y1="0" x2="1" y2="0.3">
          <stop offset="0" stop-color="#ead7d2"/>
          <stop offset="0.25" stop-color="#e7b7ae"/>
          <stop offset="0.5" stop-color="#c98482"/>
          <stop offset="0.75" stop-color="#e9b5a6"/>
          <stop offset="1" stop-color="#c77977"/>
        </linearGradient>
      </defs>
      <path d="M0 0 H1124 V186 Q600 240 0 196 Z" fill="url(#peachTone)"/>
    </svg>
    <div class="brand">Oakridge<br>Mediation</div>
    <nav class="main-nav">
      <a class="is-current" href="#">Home</a>
      <a href="#">About Us</a>
      <a href="#">About Mediation</a>
      <a href="#">Scheduling</a>
    </nav>
  </header>

  <section class="slider">
    <div class="slide slide-meeting" role="img" aria-label="Photograph of a business team meeting around a table"></div>
    <div class="slide slide-handshake" role="img" aria-label="Photograph of businessmen shaking hands after an agreement"></div>
  </section>
  <svg class="slider-arrow prev" width="44" height="44" viewBox="0 0 44 44" aria-label="Previous slide">
    <circle cx="22" cy="22" r="20" fill="var(--arrow-grey)" stroke="#fff" stroke-width="2"/>
    <path d="M25 13 L16 22 L25 31" fill="none" stroke="#fff" stroke-width="3"/>
  </svg>
  <svg class="slider-arrow next" width="44" height="44" viewBox="0 0 44 44" aria-label="Next slide">
    <circle cx="22" cy="22" r="20" fill="var(--arrow-grey)" stroke="#fff" stroke-width="2"/>
    <path d="M19 13 L28 22 L19 31" fill="none" stroke="#fff" stroke-width="3"/>
  </svg>

  <article class="feature feature-1">
    <div class="feature-thumb" role="img" aria-label="Photograph of a handshake in an office"></div>
    <h2 class="feature-title">Tur, ommodit exped esedi utam fuga.</h2>
    <div class="feature-body">
      <p class="lead">Tur seque deligent.</p>
      <p>Ro quatiam archilit as eostius, inctate lab in ratia sed molorise nes eostis duciam aut modiorum ad que rerepe rem eveleni moditat ibusam fuga. Evelecerro temporum ut odiatust, seque nitae</p>
    </div>
    <a class="feature-more" href="#">...More</a>
  </article>

  <article class="feature feature-2">
    <div class="feature-thumb" role="img" aria-label="Photograph of a handshake in an office"></div>
    <h2 class="feature-title">Tur, ommodit exped esedi utam fuga.</h2>
    <div class="feature-body">
      <p class="lead">Tur seque deligent.</p>
      <p>Ro quatiam archilit as eostius, inctate lab in ratia sed molorise nes eostis duciam aut modiorum ad que rerepe rem eveleni moditat ibusam fuga. Evelecerro temporum ut odiatust, seque nitae</p>
    </div>
    <a class="feature-more" href="#">...More</a>
  </article>

  <nav class="social">
    <a class="friendnet" href="#">friendnet</a>
    <a class="chirpline" href="#">chirpline</a>
  </nav>
</div>
</body>
</html>
```